Modernization of existing web site

Update existing web site to a professional look vs a home-made site. Site look and navigation should be up to today's standards and display properly on mobile devices.
Only simple HTML and CSS is to be used as this is a basic site. No content management.
Existing site is https://www.plexumar.example

Target Market(s)

Insurance and Technology

Industry/Entity Type

Insurance and technology

Coding

Coded - Design and coding required

Number of Pages Required

5+ page

Font styles to use
Sans Serif

Colors
0054AA
0677BA
7BADD7
CADEEF
E8F1F8
0094D4
00A9DD
6FCCEA
C7EBF8
E9F6FB

Requirements
Must have
• A sleek, modern feel and also done with a button-downed industry in mind.
Nice to have
• Clean integration of the logo and name
Should not have
• Open to ideas

```html
<!DOCTYPE html>
<html lang="en">
<head>
<meta charset="utf-8">
<title>Plexumar — Navigating Business &amp; Technology</title>
<link href="https://fonts.googleapis.com/css2?family=Poppins:wght@400;500;600;700;800&display=swap" rel="stylesheet">
<style>
:root{
  --navy:#0054AA;
  --deep:#0b2f86;
  --mid:#0677BA;
  --sky:#0094D4;
  --cyan:#00A9DD;
  --aqua:#6FCCEA;
  --pale:#CADEEF;
  --mist:#E8F1F8;
  --ink:#2b2b2b;
  --grey:#6b6b6b;
  --white:#ffffff;
}
*{box-sizing:border-box;margin:0;padding:0}
html,body{width:1200px;height:3976px;overflow:hidden}
body{font-family:"Poppins",sans-serif;color:var(--ink);background:var(--white)}
.page{position:relative;width:1200px;height:3976px;overflow:hidden}
.abs{position:absolute}
a{color:inherit;text-decoration:none}

/* header */
.topline{left:0;top:0;width:1200px;height:4px;background:var(--navy)}
.brand{display:flex;align-items:center;gap:10px;font-weight:700;font-size:34px;letter-spacing:.5px;color:var(--navy)}
.brand .mark{width:34px;height:34px;border-radius:50%;background:var(--navy)}
.header-brand{left:112px;top:40px}
.nav{left:489px;top:52px;display:flex;gap:0;font-size:13px;font-weight:500;color:#333}
.nav a{position:absolute;white-space:nowrap}
.phone-pill{left:929px;top:43px;width:159px;height:37px;border-radius:20px;background:var(--navy);color:#fff;font-size:14px;font-weight:600;display:flex;align-items:center;padding-left:8px;gap:12px}
.phone-pill .ic{width:25px;height:25px;border-radius:50%;background:#fff;display:flex;align-items:center;justify-content:center}

/* buttons */
.btn{display:flex;align-items:center;gap:12px;height:36px;border-radius:20px;background:var(--navy);color:#fff;font-size:13px;font-weight:600;padding:0 18px 0 4px;border:2px solid var(--navy)}
.btn .dot{width:28px;height:28px;border-radius:50%;background:#fff;display:flex;align-items:center;justify-content:center}
.btn .dot i{width:18px;height:18px;border-radius:50%;background:var(--ink);display:flex;align-items:center;justify-content:center}
.btn-ghost{background:var(--white);color:var(--navy)}
.btn-ghost .dot{background:var(--navy)}
.btn-ghost .dot i{background:var(--white)}

/* hero */
.hero-photo{left:0;top:122px;width:1200px;height:760px;background:linear-gradient(100deg,#c9d5db 0%,#c3d1d8 38%,#a9b9c0 55%,#7b8c8f 70%,#c0c7c7 85%,#e3e5e3 100%)}
.hero-title{left:112px;top:342px;font-size:56px;font-weight:700;line-height:68px;color:var(--ink);text-transform:uppercase}
.hero-title em{font-style:normal;color:var(--navy)}
.hero-cta{left:112px;top:579px}
.dots{left:112px;top:741px;display:flex;gap:6px}
.dots span{width:10px;height:10px;border-radius:50%;background:#fff}
.dots span:first-child{background:var(--navy)}

/* about */
.section-title{font-size:40px;font-weight:700;text-transform:uppercase;color:var(--ink)}
.section-title em{font-style:normal;color:var(--navy)}
.about-title{left:112px;top:978px}
.about-copy{left:112px;top:1066px;width:480px;font-size:14px;line-height:23.2px;color:#555}
.about-copy p{margin-bottom:23px}
.about-cta{left:112px;top:1427px}
.about-photo{left:603px;top:986px;width:486px;height:486px;border-radius:50%;background:radial-gradient(circle at 45% 40%,#6aa6d6,#1a6fb8 60%,#0b4f96);box-shadow:0 0 0 3px #fff,0 0 18px rgba(0,84,170,.25)}

/* services */
.services{left:0;top:1585px;width:1200px;height:1123px;background:linear-gradient(180deg,#0a78cc 0%,#0b8ad8 50%,#0a7fd0 100%)}
.services-title{left:0;top:1675px;width:1200px;text-align:center;color:#fff;font-size:40px;font-weight:700}
.card-img{width:300px;height:152px}
.card-body{width:270px;height:208px;background:#fff;padding:36px 34px 0}
.card-body h3{font-size:13.5px;font-weight:600;line-height:21px;text-transform:uppercase;color:#222;margin-bottom:14px}
.card-body p{font-size:11px;line-height:20px;color:#666}
.learn{display:flex;align-items:center;gap:10px;margin-top:10px;font-size:11.5px;font-weight:600;color:var(--navy);text-decoration:underline}
.learn i{width:13px;height:13px;border-radius:50%;background:var(--navy);display:inline-block}
.card-feature{width:300px;height:360px;background:linear-gradient(180deg,#4e6070,#7a8a98 55%,#3d6ea0)}
.feature-box{position:absolute;left:14px;top:146px;width:272px;height:202px;background:#fff;border:3px solid #cde2f3;outline:2px solid var(--cyan);outline-offset:-8px;text-align:center;padding:28px 20px 0}
.feature-box h3{font-size:13.5px;font-weight:600;line-height:21px;text-transform:uppercase;color:#222;margin-bottom:14px}
.feature-box p{font-size:11px;line-height:20px;color:#666}
.feature-box .learn{justify-content:center}
.services-ctas{left:446px;top:2584px;display:flex;gap:20px}
.btn-white{background:#fff;color:var(--navy);border-color:#fff}
.btn-white .dot{background:var(--navy)}
.btn-white .dot i{background:#fff}
.btn-outline{background:transparent;color:#fff;border-color:#fff}

/* testimonials */
.testi-title{left:0;top:2783px;width:1200px;text-align:center}
.quote-mark{font-size:80px;font-weight:700;color:var(--navy);line-height:1}
.testi-text{left:270px;top:2910px;width:660px;text-align:center;font-size:14px;line-height:28px;color:#777}
.arrow{width:28px;height:28px;border-radius:50%;border:1px solid #bbb;display:flex;align-items:center;justify-content:center}
.person{display:flex;align-items:center;gap:12px}
.person .av{width:50px;height:50px;border-radius:50%;background:linear-gradient(135deg,#d9dfe4,#aeb8c0)}
.person b{display:block;font-size:15px;font-weight:600;color:var(--aqua)}
.person span{font-size:13px;color:#c4c4c4}
.person.active b{color:var(--navy)}
.person.active span{color:#555}
.person.active .av{background:linear-gradient(135deg,#7a98b5,#3b5e84)}
.underline{left:500px;top:3126px;width:198px;height:2px;background:#222}

/* footer */
.footer-shape{left:0;top:3260px}
.inquiry{left:702px;top:3296px;width:386px;height:428px;background:#fff;border-radius:10px;box-shadow:0 4px 30px rgba(0,40,100,.15);padding:38px 43px 0}
.inquiry h2{text-align:center;font-size:30px;font-weight:700;color:#222;margin-bottom:22px}
.inquiry h2 em{font-style:normal;color:var(--navy)}
.field{height:52px;border:1px solid #ccc;border-radius:4px;font-size:14px;color:#666;padding:15px 22px;margin-bottom:16px}
.field.tall{height:112px}
.inquiry .btn{margin:27px auto 0;width:146px}
.footer-brand{left:112px;top:3555px;color:#fff}
.footer-brand .mark{background:#fff}
.f-head{font-size:19px;font-weight:700;color:#fff;text-transform:uppercase;text-decoration:underline;text-underline-offset:5px}
.quick-links{left:438px;top:3490px}
.quick-links ul{list-style:none;margin-top:22px}
.quick-links li{font-size:12.5px;font-weight:500;color:#fff;margin-bottom:11px;text-transform:uppercase}
.contact-head{left:112px;top:3682px}
.info{display:flex;align-items:center;gap:16px;color:#fff}
.info .ic{width:46px;height:46px;border-radius:50%;background:#fff;display:flex;align-items:center;justify-content:center}
.info b{display:block;font-size:14px;font-weight:600;margin-bottom:5px}
.info span{font-size:13px;line-height:22px}
.copyright{left:112px;top:3903px;font-size:13px;color:#fff}
.socials{left:929px;top:3896px;display:flex;gap:15px}
.socials span{width:28px;height:28px;border-radius:50%;background:#fff;display:block}
</style>
</head>
<body>
<div class="page">

  <!-- header -->
  <div class="abs topline"></div>
  <div class="abs brand header-brand"><span class="mark"></span>PLEXUMAR</div>
  <nav class="abs nav">
    <a style="left:0">HOME</a>
    <a style="left:91px">ABOUT US</a>
    <a style="left:209px">SERVICES</a>
    <a style="left:324px">CONTACT US</a>
  </nav>
  <div class="abs phone-pill">
    <span class="ic"><svg width="14" height="14" viewBox="0 0 24 24"><path fill="#0054AA" d="M6.6 10.8a15.1 15.1 0 0 0 6.6 6.6l2.2-2.2a1 1 0 0 1 1-.25 11.4 11.4 0 0 0 3.6.57 1 1 0 0 1 1 1V20a1 1 0 0 1-1 1A17 17 0 0 1 3 4a1 1 0 0 1 1-1h3.5a1 1 0 0 1 1 1c0 1.25.2 2.45.57 3.57a1 1 0 0 1-.25 1z"/></svg></span>
    555-014-2290
  </div>

  <!-- hero -->
  <div class="abs hero-photo" role="img" aria-label="Photo of two colleagues reviewing papers at a laptop in a bright glass-walled office"></div>
  <svg class="abs" style="left:0;top:122px" width="1200" height="780" viewBox="0 0 1200 780">
    <path d="M0 418 C40 590 160 760 340 746 C520 732 610 560 830 580 C990 595 1080 728 1200 716 L1200 780 L0 780 Z" fill="#ffffff"/>
    <path d="M0 418 C40 590 160 760 340 746 C520 732 610 560 830 580 C990 595 1080 728 1200 716" fill="none" stroke="#00A9DD" stroke-width="2.5"/>
  </svg>
  <h1 class="abs hero-title">Navigating <em>Business</em><br><em>&amp; Technology</em> to<br>Generate Results</h1>
  <a class="abs btn hero-cta"><span class="dot"><i><svg width="10" height="10" viewBox="0 0 10 10"><path d="M2 5h6M5.5 2.5 8 5 5.5 7.5" stroke="#fff" stroke-width="1.4" fill="none"/></svg></i></span>GET STARTED</a>
  <div class="abs dots"><span></span><span></span><span></span><span></span></div>

  <!-- about -->
  <h2 class="abs section-title about-title">About <em>Plexumar</em></h2>
  <div class="abs about-copy">
    <p>Plexumar was formed in late 2018 to bring over 35 years of experience in multiple industries and disciplines to our customers.</p>
    <p>Dale Warren has led large and small organizations. With senior executive experience in business and technology, he has a distinct view of the business and technology needs of organizations.</p>
    <p>Dale has spent the last 20 years in various senior leadership positions at a leading property &amp; casualty insurance group, most recently as Chairman and President. He spent the early years of his career in high-tech manufacturing. He has also invested in several technology start-up's. Since 2011, Dale has served as an independent director at one of the nation's leading publicly traded financial services companies.</p>
  </div>
  <a class="abs btn about-cta"><span class="dot"><i><svg width="10" height="10" viewBox="0 0 10 10"><path d="M2 5h6M5.5 2.5 8 5 5.5 7.5" stroke="#fff" stroke-width="1.4" fill="none"/></svg></i></span>READ MORE</a>
  <div class="abs about-photo" role="img" aria-label="Blue-toned photo of a team collaborating around laptops in a casual office"></div>

  <!-- services -->
  <div class="abs services" role="img" aria-label="Blue background with soft technology imagery"></div>
  <h2 class="abs services-title">OUR SERVICES</h2>

  <div class="abs card-img" style="left:112px;top:1776px;background:linear-gradient(135deg,#3a4a52,#8c9aa0 50%,#dfe4e6)" role="img" aria-label="Two professionals planning at a glass board"></div>
  <div class="abs card-body" style="left:112px;top:1928px">
    <h3>Business and Technology Strategy</h3>
    <p>Lorem ipsum dolor sit amet, consectetur adipiscing elit, sed do eiusmod tempor incididunt.</p>
    <a class="learn">Learn More <i></i></a>
  </div>

  <div class="abs card-feature" style="left:450px;top:1776px" role="img" aria-label="Team members reviewing documents together on a table">
    <div class="feature-box">
      <h3>Distribution Channel Development</h3>
      <p>Lorem ipsum dolor sit amet, consectetur adipiscing elit, sed do eiusmod tempor incididunt.</p>
      <a class="learn">Learn More <i></i></a>
    </div>
  </div>

  <div class="abs card-img" style="left:788px;top:1776px;background:linear-gradient(135deg,#2c2c2c,#6a7078 45%,#2f6fb8 75%,#c0c8d0)" role="img" aria-label="Hand writing on papers next to a blue compliance binder"></div>
  <div class="abs card-body" style="left:788px;top:1928px">
    <h3>Rating and Regulatory</h3>
    <p>Lorem ipsum dolor sit amet, consectetur adipiscing elit, sed do eiusmod tempor incididunt.</p>
    <a class="learn">Learn More <i></i></a>
  </div>

  <div class="abs card-img" style="left:112px;top:2177px;background:linear-gradient(135deg,#5a4030,#b78a66 50%,#e8d8c8)" role="img" aria-label="Hands shielding a wooden chess king"></div>
  <div class="abs card-body" style="left:112px;top:2329px">
    <h3>Enterprise Risk Management</h3>
    <p>Lorem ipsum dolor sit amet, consectetur adipiscing elit, sed do eiusmod tempor incididunt.</p>
    <a class="learn">Learn More <i></i></a>
  </div>

  <div class="abs card-img" style="left:450px;top:2177px;background:linear-gradient(135deg,#0d1d3a,#23497e 55%,#0e2244)" role="img" aria-label="Professional interacting with a digital data display"></div>
  <div class="abs card-body" style="left:450px;top:2329px">
    <h3>Data/Reporting/<br>Analytics</h3>
    <p>Lorem ipsum dolor sit amet, consectetur adipiscing elit, sed do eiusmod tempor incididunt.</p>
    <a class="learn">Learn More <i></i></a>
  </div>

  <div class="abs card-img" style="left:788px;top:2177px;background:linear-gradient(135deg,#1d2a3a,#4b5a6c 50%,#d8dce2)" role="img" aria-label="Hand touching a project timeline on a digital screen"></div>
  <div class="abs card-body" style="left:788px;top:2329px">
    <h3>Technology Implementation</h3>
    <p>Lorem ipsum dolor sit amet, consectetur adipiscing elit, sed do eiusmod tempor incididunt.</p>
    <a class="learn">Learn More <i></i></a>
  </div>

  <div class="abs services-ctas">
    <a class="btn btn-white"><span class="dot"><i><svg width="10" height="10" viewBox="0 0 10 10"><path d="M2 5h6M5.5 2.5 8 5 5.5 7.5" stroke="#0054AA" stroke-width="1.4" fill="none"/></svg></i></span>VIEW MORE</a>
    <a class="btn btn-outline"><span class="dot" style="background:#fff"><i style="background:#0054AA"><svg width="10" height="10" viewBox="0 0 10 10"><path d="M2 5h6M5.5 2.5 8 5 5.5 7.5" stroke="#fff" stroke-width="1.4" fill="none"/></svg></i></span>GET STARTED</a>
  </div>

  <!-- testimonials -->
  <h2 class="abs section-title testi-title">Happy <em>Customers</em></h2>
  <div class="abs quote-mark" style="left:235px;top:2865px">&ldquo;</div>
  <p class="abs testi-text">Lorem ipsum dolor sit amet, consectetur adipiscing elit, sed do eiusmod tempor incididunt ut et dolore magna aliqua. Ut enim ad minim veniam, quis nostrud exercitation ullamco laboris nisi ut aliquip ex ea commodo consequat.Duis aute irure dolor in reprehenderit in voluptate</p>
  <div class="abs quote-mark" style="left:908px;top:2978px">&rdquo;</div>
  <div class="abs arrow" style="left:65px;top:2993px"><svg width="10" height="10" viewBox="0 0 10 10"><path d="M6.5 1.5 3 5l3.5 3.5" stroke="#999" fill="none"/></svg></div>
  <div class="abs arrow" style="left:1107px;top:2993px"><svg width="10" height="10" viewBox="0 0 10 10"><path d="M3.5 1.5 7 5 3.5 8.5" stroke="#999" fill="none"/></svg></div>
  <div class="abs person" style="left:249px;top:3059px"><span class="av" role="img" aria-label="Customer portrait"></span><div><b>CALVIN</b><span>Position Name</span></div></div>
  <div class="abs person active" style="left:515px;top:3059px"><span class="av" role="img" aria-label="Customer portrait"></span><div><b>DORIAN</b><span>Position Name</span></div></div>
  <div class="abs person" style="left:782px;top:3059px"><span class="av" role="img" aria-label="Customer portrait"></span><div><b>FELIX</b><span>Position Name</span></div></div>
  <div class="abs underline"></div>

  <!-- footer -->
  <svg class="abs footer-shape" width="1200" height="716" viewBox="0 0 1200 716">
    <defs>
      <linearGradient id="footerFill" x1="0" y1="0" x2="1" y2="1">
        <stop offset="0" stop-color="#0b3a9a"/>
        <stop offset="1" stop-color="#0a2f86"/>
      </linearGradient>
    </defs>
    <path d="M0 330 C60 140 190 30 320 30 C470 32 560 205 720 220 L1090 220 L1090 110 C1130 80 1170 70 1200 76 L1200 716 L0 716 Z" fill="url(#footerFill)"/>
    <path d="M0 330 C60 140 190 30 320 30 C470 32 560 205 720 220" fill="none" stroke="#00A9DD" stroke-width="2.5"/>
    <path d="M1090 110 C1130 80 1170 70 1200 76" fill="none" stroke="#00A9DD" stroke-width="2.5"/>
  </svg>

  <div class="abs inquiry">
    <h2>QUICK <em>INQUIRY</em></h2>
    <div class="field">Your Name*</div>
    <div class="field">Email Address*</div>
    <div class="field tall">Your Message Here .....</div>
    <a class="btn"><span class="dot"><i><svg width="10" height="10" viewBox="0 0 10 10"><path d="M2 5h6M5.5 2.5 8 5 5.5 7.5" stroke="#fff" stroke-width="1.4" fill="none"/></svg></i></span>SEND NOW</a>
  </div>

  <div class="abs brand footer-brand"><span class="mark"></span>PLEXUMAR</div>

  <div class="abs quick-links">
    <div class="f-head">Quick Links</div>
    <ul><li>Home</li><li>About Us</li><li>Our Services</li><li>Contact Us</li></ul>
  </div>

  <div class="abs f-head contact-head">Contact Info</div>
  <div class="abs info" style="left:112px;top:3734px">
    <span class="ic"><svg width="18" height="18" viewBox="0 0 24 24"><path fill="#0054AA" d="M6.6 10.8a15.1 15.1 0 0 0 6.6 6.6l2.2-2.2a1 1 0 0 1 1-.25 11.4 11.4 0 0 0 3.6.57 1 1 0 0 1 1 1V20a1 1 0 0 1-1 1A17 17 0 0 1 3 4a1 1 0 0 1 1-1h3.5a1 1 0 0 1 1 1c0 1.25.2 2.45.57 3.57a1 1 0 0 1-.25 1z"/></svg></span>
    <div><b>Phone Number</b><span>555-014-2290</span></div>
  </div>
  <div class="abs info" style="left:112px;top:3802px">
    <span class="ic"><svg width="18" height="18" viewBox="0 0 24 24"><rect x="3" y="6" width="18" height="12" rx="2" fill="#0054AA"/><path d="M3 7l9 6 9-6" stroke="#fff" stroke-width="1.5" fill="none"/></svg></span>
    <div><b>Email Address</b><span>info@plexumar.example</span></div>
  </div>
  <div class="abs info" style="left:430px;top:3734px">
    <span class="ic"><svg width="18" height="18" viewBox="0 0 24 24"><path fill="#0054AA" d="M12 2a7 7 0 0 0-7 7c0 5 7 13 7 13s7-8 7-13a7 7 0 0 0-7-7zm0 9.5A2.5 2.5 0 1 1 12 6.5a2.5 2.5 0 0 1 0 5z"/></svg></span>
    <div><span>42 Cedar Hollow Ln<br>Riverton, NV 89000</span></div>
  </div>
  <div class="abs info" style="left:430px;top:3802px">
    <span class="ic"><svg width="18" height="18" viewBox="0 0 24 24"><rect x="3" y="7" width="18" height="12" rx="2" fill="#0054AA"/><path d="M9 7V5h6v2" stroke="#0054AA" stroke-width="2" fill="none"/></svg></span>
    <div><b>Working Hours</b><span>Mon – Fri: 9:00 – 5:00</span></div>
  </div>

  <div class="abs copyright">Copyright © 2022 Plexumar . All Right Reserved</div>
  <div class="abs socials" aria-label="Social links"><span></span><span></span><span></span><span></span></div>

</div>
</body>
</html>
```